依頼詳細
商品は布マスクになりますが、取り急ぎ添付の不織布マスクの内容で構いせん。
全体のイメージで決定したいと思います。
決定後に布マスクの詳細をお伝えしますので、完成品に仕上げて頂きたいと思います。

製品形状はPP袋(PPのベースは透明もしくはアルミ銀)
袋サイズ:W130xH180mm+ヘッダー部分H20mm

印刷は4色分解でも構いませんが、中国印刷の為、あまり複雑過ぎない程度の色使いでお願いします。

急ぎ提案なのでイメージだけでも早く提案してもらえば助かります。
説明不足で申し訳ございませんが、不明点はご連絡お願い致します。
記載項目
PP袋(PPのベースは透明もしくはアルミ銀)

印刷は4色分解でも構いませんが、中国グラビア印刷(8色まで)の為、あまり複雑過ぎない程度の色使いでお願いします。版代のコストも抑えたいです。
希望イメージ
シンプル 複雑
単色 カラフル
暗い 明るい
日常 高級
遊び心 厳粛
未来的 伝統的
女性的 男性的
希望する色
青系、水色系、無彩色系
納品ファイル
• イラストレーター形式 (.ai)
補足説明

お客様の選定により

たくさんのご提案ありがとうございました
またの機会にも是非またご提案お願い致します。

```html
<!DOCTYPE html>
<html lang="ja">
<head>
<meta charset="utf-8">
<title>3層 布製マスク パッケージ</title>
<link href="https://fonts.googleapis.com/css2?family=Noto+Sans+JP:wght@400;500;700;900&display=swap" rel="stylesheet">
<style>
  :root {
    --navy: #1d3c86;
    --ink: #111111;
    --sky: #4fb3df;
    --sky-pale: #c4e8f6;
    --silver: #e9edf1;
    --line: #9aa3ad;
    --white: #ffffff;
  }
  * { margin: 0; padding: 0; box-sizing: border-box; }
  html, body { width: 775px; height: 1200px; overflow: hidden; background: var(--white); }
  body { font-family: "Noto Sans JP", sans-serif; color: var(--ink); position: relative; }
  .abs { position: absolute; }

  .base-note { left: 13px; top: 14px; font-size: 24px; font-weight: 500; }

  .bag { left: 36px; top: 57px; width: 713px; height: 1120px; border: 2px solid var(--line); background: var(--white); overflow: hidden; }
  .hang-slot { left: 312px; top: 24px; width: 150px; height: 22px; border: 2px solid var(--line); border-radius: 11px; }
  .wave-top { right: 0; top: 0; width: 330px; height: 380px;
    background: radial-gradient(ellipse at 80% 20%, rgba(79,179,223,.35), rgba(196,232,246,.15) 55%, transparent 75%); }
  .wave-bottom { left: 0; bottom: 0; width: 420px; height: 300px;
    background: radial-gradient(ellipse at 20% 85%, rgba(79,179,223,.35), rgba(196,232,246,.15) 55%, transparent 75%); }

  .origin { left: 57px; top: 155px; width: 90px; height: 34px; border: 2px solid var(--ink); font-size: 21px; font-weight: 700; display: flex; align-items: center; justify-content: center; }

  .size-tag { left: 509px; top: 150px; width: 111px; height: 49px; border: 2px solid var(--navy); text-align: center; line-height: 1; }
  .size-tag .size-name { display: block; background: var(--sky); color: var(--white); font-size: 20px; font-weight: 700; padding: 3px 0; }
  .size-tag .size-name small { font-size: 11px; }
  .size-tag .size-dim { display: block; font-size: 11px; padding-top: 4px; }
  .count-tag { left: 625px; top: 150px; width: 104px; height: 49px; border: 2px solid var(--navy); display: flex; align-items: baseline; justify-content: center; padding-top: 4px; color: var(--navy); font-weight: 700; }
  .count-tag .num { font-size: 32px; }
  .count-tag .unit { font-size: 18px; }

  .blocks { left: 0; width: 775px; text-align: center; font-size: 25px; font-weight: 500; top: 252px; }
  .headline { left: 0; width: 775px; text-align: center; font-size: 40px; font-weight: 900; top: 288px; letter-spacing: 1px; }

  .layer-box { left: 176px; top: 346px; width: 88px; height: 166px; background: var(--navy); color: var(--white); display: flex; flex-direction: column; align-items: center; justify-content: center; font-weight: 900; line-height: 1; }
  .layer-box .num { font-size: 82px; }
  .layer-box .kanji { font-size: 56px; margin-top: 4px; }
  .material { left: 264px; top: 346px; width: 330px; height: 70px; border: 3px solid var(--navy); color: var(--navy); font-size: 60px; font-weight: 900; display: flex; align-items: center; justify-content: center; letter-spacing: 14px; line-height: 1; }
  .product { left: 264px; top: 416px; width: 330px; height: 96px; background: var(--navy); color: var(--white); font-size: 78px; font-weight: 900; display: flex; align-items: center; justify-content: center; letter-spacing: 4px; line-height: 1; }

  .moisture-badge { left: 172px; top: 518px; width: 96px; height: 104px; border-radius: 16px; background: var(--sky); color: var(--white); font-size: 21px; font-weight: 900; line-height: 1.3; display: flex; align-items: center; justify-content: center; text-align: center; }
  .droplet { left: 274px; top: 522px; color: var(--navy); font-weight: 900; font-size: 34px; line-height: 1; white-space: nowrap; }
  .droplet .pct { font-size: 44px; }
  .filter-band { left: 274px; top: 574px; width: 326px; height: 42px; background: var(--sky-pale); color: var(--navy); font-size: 28px; font-weight: 900; display: flex; align-items: center; padding-left: 10px; }

  .mask-art { left: 100px; top: 650px; width: 500px; height: 360px; border-radius: 40px;
    background: linear-gradient(160deg, #f7f9fb, #dfe6ec); }
  .leaders { left: 0; top: 0; }
  .note { font-size: 16px; line-height: 1.35; font-weight: 500; }
  .note-nose { left: 462px; top: 655px; }
  .note-ear { left: 598px; top: 672px; }
  .note-pleat { left: 112px; top: 1000px; }
</style>
</head>
<body>
  <div class="abs base-note">パック地:シルバー</div>

  <div class="abs bag">
    <div class="abs hang-slot"></div>
    <div class="abs wave-top" role="img" aria-label="青い流線の装飾"></div>
    <div class="abs wave-bottom" role="img" aria-label="青い流線の装飾"></div>
  </div>

  <div class="abs origin">日本製</div>
  <div class="abs size-tag"><span class="size-name">ふつう<small>サイズ</small></span><span class="size-dim">約17.5×9.5cm</span></div>
  <div class="abs count-tag"><span class="num">3</span><span class="unit">枚入</span></div>

  <div class="abs blocks">花粉・ウイルス粉末・ハウスダスト・PM2.5</div>
  <div class="abs headline">高密度フィルターがブロック</div>

  <div class="abs layer-box"><span class="num">3</span><span class="kanji">層</span></div>
  <div class="abs material">布製</div>
  <div class="abs product">マスク</div>

  <div class="abs moisture-badge">空気中<br>水分を<br>含んだ</div>
  <div class="abs droplet">ウィルス飛沫<span class="pct">99%</span></div>
  <div class="abs filter-band">カットフィルター使用</div>

  <div class="abs mask-art" role="img" aria-label="三段プリーツの白いマスクのイラスト"></div>

  <svg class="abs leaders" width="775" height="1200" aria-hidden="true">
    <g stroke="#333" stroke-width="1.5" fill="none">
      <line x1="470" y1="700" x2="420" y2="740"/>
      <line x1="600" y1="720" x2="560" y2="790"/>
      <line x1="140" y1="995" x2="180" y2="940"/>
    </g>
  </svg>

  <div class="abs note note-nose">ノーズワイヤ／<br>鼻にぴったり</div>
  <div class="abs note note-ear">耳掛ゴム<br>耳が痛くなりにくい<br>ソフトゴム</div>
  <div class="abs note note-pleat">三段プリーツ構造</div>
</body>
</html>
```